Smart, Classy, Conservative looking Legal Letterhead

I need a letterhead that when you look at it it "says to you " this is a well established law firm with very smart lawyers, which will one day be appearing before the Supreme Court of the USA. All information about the Law firm should appear at the top of the page. please no information in the footer.

Industry/Entity Type

Legal

Requirements
Must have
• The name of the law firm, both addresses, phone number and fax,, The names of the attorneys, the website.
• Fields that get changed such as the date, VIA, Address of who the letter is going to,
• Re, Index,
• should have a clean neat look, sleek
Nice to have
• some color would be nice. A logo of some sort could be nice as well. Maybe a single S or interlocking B's For Brevik and Brevik.
Should not have
• not too modern looking.

```html
<!DOCTYPE html>
<html lang="en">
<head>
<meta charset="utf-8">
<title>Brevik &amp; Brevik Letterhead</title>
<link rel="stylesheet" href="https://fonts.googleapis.com/css2?family=Cinzel:wght@400;600&family=Carlito:wght@400;700&display=swap">
<style>
  :root {
    --ink: #1b1b1b;
    --accent: #5d7fb8;
    --rule: #444444;
    --paper: #ffffff;
  }
  * { margin: 0; padding: 0; box-sizing: border-box; }
  html, body { width: 1200px; height: 757px; overflow: hidden; background: var(--paper); }
  .letterhead { position: relative; width: 1200px; height: 757px; background: var(--paper); color: var(--ink); }

  .office {
    position: absolute; top: 50px;
    font-family: "Cinzel", serif; font-style: normal; font-size: 17px; line-height: 21.8px;
    color: var(--accent);
  }
  .office--left { left: 55px; text-align: left; }
  .office--right { right: 54px; text-align: right; }
  .office .tel { font-size: 15px; }

  .firm-name {
    position: absolute; top: 70px; left: 0; width: 1200px; text-align: center;
    font-family: "Cinzel", serif; font-weight: 400; font-size: 40px; letter-spacing: 0.5px;
    color: var(--ink); line-height: 1;
  }
  .firm-tagline {
    position: absolute; top: 110px; left: 620px;
    font-family: "Cinzel", serif; font-size: 18px; color: var(--accent); letter-spacing: 0.5px;
  }
  .website {
    position: absolute; top: 172px; left: 0; width: 1200px; text-align: center;
    font-family: "Cinzel", serif; font-size: 11px; color: var(--accent); letter-spacing: 0.6px;
  }
  .header-rule { position: absolute; top: 194px; left: 51px; width: 1097px; height: 2px; background: var(--rule); }

  .attorneys {
    position: absolute; top: 208px; left: 0; width: 1200px; height: 24px;
    font-family: "Cinzel", serif; font-weight: 600; font-size: 15px; color: var(--accent); list-style: none;
  }
  .attorneys li { position: absolute; top: 0; white-space: nowrap; }

  .letter { font-family: "Carlito", sans-serif; font-size: 18.5px; color: var(--ink); }
  .letter .line { position: absolute; left: 77px; line-height: 26px; white-space: nowrap; }
  .delivery { font-weight: 700; text-decoration: underline; }
  .ref-label { position: absolute; left: 215px; font-weight: 700; line-height: 26px; }
  .ref-value { position: absolute; left: 355px; line-height: 26px; }
  .ref-value--underlined { text-decoration: underline; }
  .letter .indent { left: 147px; }
  .letter .signature { left: 565px; }
</style>
</head>
<body>
<main class="letterhead">
  <header>
    <address class="office office--left">
      47 Linden Row<br>
      New York, New York 10004<br>
      <span class="tel">p 914-555-0181</span><br>
      <span class="tel">f 914-555-0930</span>
    </address>

    <h1 class="firm-name">Brevik &amp; Brevik</h1>
    <p class="firm-tagline">Attorneys at Law</p>

    <address class="office office--right">
      212 Orchard Road<br>
      Westbrook, New York 10579<br>
      <span class="tel">p 914-555-0181</span><br>
      <span class="tel">f 914-555-0930</span>
    </address>

    <p class="website">www.newyorkclientadvocates.com</p>
    <div class="header-rule"></div>

    <ul class="attorneys">
      <li style="left:77px">Thomas Brevik, Esq.</li>
      <li style="left:341px">Daniel A. Brevik, Esq.</li>
      <li style="left:615px">Elizabeth Hallorann, Esq.</li>
      <li style="left:937px">Peter T. Marsh, Esq.</li>
    </ul>
  </header>

  <section class="letter">
    <p class="line" style="top:273px">October 14, 2014</p>

    <p class="line delivery" style="top:325px">VIA SWIFTPOST</p>
    <p class="line" style="top:350px">Hon. Fake Judge Name Here</p>
    <p class="line" style="top:376px">United States District Court, E.D.N.Y.</p>
    <p class="line" style="top:402px">250 Harbor Plaza</p>
    <p class="line" style="top:428px">Courtroom XXXXX</p>
    <p class="line" style="top:454px">Eastport, NY 11941-0000</p>

    <p class="ref-label" style="top:480px">Re:</p>
    <p class="ref-value ref-value--underlined" style="top:480px">XXXXXXXXXXXXXXXXXXX</p>
    <p class="ref-label" style="top:506px">Index:</p>
    <p class="ref-value" style="top:506px">XXXXXXXX</p>

    <p class="line" style="top:532px">Your Honor:</p>
    <p class="line indent" style="top:558px">Pursuant to Your Honor’s Individual Practices Rule III(C)(3), enclosed please find a courtesy copy of Plaintiff’s</p>
    <p class="line" style="top:584px">Revised Yadda Yadda Yadda.</p>
    <p class="line" style="top:609px">Respectfully,</p>
    <p class="line signature" style="top:636px">Daniel A. Brevik</p>

    <p class="line" style="top:688px">cc:&nbsp; fake opposing counsel name here.</p>
  </section>
</main>
</body>
</html>
```